Wheels Open Doors - Two sided invitation to encourage bike friendly businesses

Pedal Haven is a charitable trust who want to grow everyday bike use. One way to do that is help businesses understand that 'Wheels Open Doors'. We want a postcard sized 'invitation' that bike users can give to their favourite businesses, inviting them to find out more about all the benefits of attracting bike users to their business and becoming a 'Pedal Haven Business'. We are currently finalising copy, so the attached is indicative but not final copy. The docx file is the words, the png is indicative of the type of infographic we might want to feature.
I'm also attaching a mock up of our window sticker for businesses, and some social shares featuring photographic images which we have available to use. This will give you an idea of our branding to date. Our extended branding concept (which we will use when we re-do our website) is based on icons, so I'm open to seeing icon focused designs also.
The feel needs to be inviting, credible, enticing, business like, noticeable, with a strong call to action.

Target Market(s)

Small business operators: retail, cafes, etc; also managers of larger chains such as supermarkets, gyms, etc.

Industry/Entity Type

Non Profit

Font styles to use
Serif
Other font styles liked:
• Logo is done in Raleway, so need compatible font.

Colors
9ccb3b

Requirements
Must have
• Two Sides
• Use the copy provided
• Strong call to action - visiting website
• Use our colours
• A6 sized cards
Nice to have
• Compelling images and/or infographic
• Consistency with circles / curves used in other branding.
Should not have
• Not bland, not something that will get lost on the recipients desk or counter.

```html
<!DOCTYPE html>
<html lang="en">
<head>
<meta charset="utf-8">
<title>Pedal Haven – Business Invitation Card</title>
<link href="https://fonts.googleapis.com/css2?family=Raleway:wght@400;500&family=Lato:wght@400;700&family=Oswald:wght@400&family=Nunito:wght@800&display=swap" rel="stylesheet">
<style>
  :root{
    --green:#9ccb3b;
    --green-deep:#5fae2e;
    --green-text:#7cbf2f;
    --ink:#222;
    --grey-dark:#3a3a3a;
    --grey-mid:#8a8a8a;
    --grey-light:#f1f1f1;
    --paper:#ffffff;
    --stage:#e9e7e2;
  }
  *{box-sizing:border-box;margin:0;padding:0}
  html,body{width:1200px;height:1200px;overflow:hidden;background:var(--stage)}
  .canvas{position:relative;width:1200px;height:1200px}
  .card{position:absolute;top:211px;width:553px;height:778px;background:var(--paper);overflow:hidden;box-shadow:0 2px 8px rgba(0,0,0,.18)}
  .card--front{left:34px}
  .card--back{left:613px}
  .card__shapes{position:absolute;inset:0;width:553px;height:778px}

  /* front */
  .brand{position:absolute;top:128px;left:0;right:0;display:flex;justify-content:center;align-items:center;gap:12px}
  .brand__dot{width:70px;height:70px;border-radius:50%;border:5px solid var(--grey-mid);background:var(--paper)}
  .brand__name{font-family:"Raleway",sans-serif;font-weight:500;font-size:34px;color:var(--green-deep)}
  .headline{position:absolute;top:240px;left:0;right:0;text-align:center;font-family:"Raleway",sans-serif;color:var(--ink)}
  .headline__line{font-size:31px;line-height:39px;font-weight:500}
  .headline__accent{display:flex;align-items:center;justify-content:center;gap:18px;color:var(--green-deep);font-size:38px;line-height:40px}
  .headline__accent::before,.headline__accent::after{content:"";width:66px;height:2px;background:var(--green-deep)}

  .compare{position:absolute;left:41px;width:317px;border:2px solid #bbb;border-radius:10px;background:var(--paper)}
  .compare--car{top:387px;height:132px}
  .compare--bike{top:531px;height:132px}
  .art{position:absolute;border-radius:6px;background:linear-gradient(#f4fae8,#e6f2cf)}
  .compare--car .art{left:14px;top:14px;width:290px;height:104px}
  .compare--bike .art{left:16px;top:76px;width:318px;height:42px}
  .tag{position:absolute;border:1.5px solid #333;border-radius:4px;background:var(--paper);font-family:"Oswald",sans-serif;text-align:center;color:#222;width:50px;height:44px;padding-top:3px}
  .tag b{display:block;font-weight:400;font-size:16px;line-height:19px}
  .tag span{display:block;font-size:9px;line-height:12px}
  .compare--car .tag{right:12px;top:10px;z-index:1}
  .tag-row{position:absolute;left:10px;top:16px;display:flex;gap:5px}
  .tag-row .tag{position:static}
  .compare--bike{width:370px}
  .compare--bike .art{width:340px}

  .price{position:absolute;left:415px;width:97px;height:132px;border-radius:10px;background:var(--green);color:#fff;font-family:"Oswald",sans-serif;padding:10px 0 0 12px}
  .price--car{top:387px}
  .price--bike{top:531px}
  .price__till{width:38px;height:32px;border:3px solid #222;border-radius:3px}
  .price__area{position:absolute;right:10px;top:40px;font-size:13px;color:#222}
  .price__amount{font-size:31px;line-height:34px;margin-top:12px}
  .price__unit{font-size:21px;line-height:24px}
  .compare--bike{width:370px}
  .price--bike{left:415px}

  .source{position:absolute;left:41px;top:675px;width:471px;height:34px;border-radius:10px;background:var(--grey-dark);color:#fff;font-family:"Lato",sans-serif;font-size:12.5px;line-height:34px;text-align:center}
  .footer-url{position:absolute;left:0;right:0;top:738px;height:36px;line-height:36px;text-align:center;color:#fff;font-family:"Lato",sans-serif;font-size:19px;letter-spacing:3.5px}

  /* back */
  .photo-wash{position:absolute;left:0;top:120px;width:553px;height:560px;background:linear-gradient(180deg,rgba(235,235,235,.0),rgba(225,225,225,.55) 50%,rgba(235,235,235,0))}
  .back-title{position:absolute;left:41px;top:94px;font-family:"Nunito",sans-serif;font-weight:800;font-size:25px;color:var(--green-text)}
  .reasons{position:absolute;left:41px;top:148px;width:480px;list-style:none;font-family:"Lato",sans-serif;font-size:16px;line-height:20px;color:var(--ink)}
  .reasons li{position:relative;padding-left:37px;min-height:32px;margin-bottom:12px;display:flex;align-items:center}
  .reasons li::before{content:"";position:absolute;left:0;top:50%;margin-top:-16px;width:32px;height:32px;border-radius:50%;background:var(--grey-dark);box-shadow:inset 0 0 0 9px var(--grey-dark),inset 0 0 0 20px var(--green)}
  .study{position:absolute;left:41px;top:414px;width:480px;font-family:"Lato",sans-serif;color:var(--ink)}
  .study__lead{font-family:"Raleway",sans-serif;font-weight:500;font-size:23px;line-height:27px}
  .study__rest{font-size:19.5px;line-height:24px}
  .study__figure{font-weight:700;font-size:38px;line-height:44px;color:var(--green-text)}
  .prompt{position:absolute;left:41px;top:556px;width:471px;height:63px;border:1.5px solid #555;border-radius:16px;background:var(--paper);text-align:center;font-family:"Lato",sans-serif;font-size:20px;line-height:26px;padding-top:5px;color:var(--ink)}
  .prompt em{font-style:normal;font-weight:700;color:var(--green-text)}
  .cta{position:absolute;left:41px;top:705px;font-family:"Lato",sans-serif;color:var(--ink)}
  .cta__line{display:flex;align-items:center;gap:7px;font-size:25px;font-weight:700}
  .cta__globe{width:24px;height:24px}
  .cta__url{color:#fff}
  .cta__sub{font-size:19.5px;line-height:24px;margin-top:2px}
</style>
</head>
<body>
<div class="canvas">

  <!-- front side -->
  <section class="card card--front">
    <svg class="card__shapes" viewBox="0 0 553 778" aria-hidden="true">
      <defs>
        <linearGradient id="greyTop" x1="0" y1="0" x2="0" y2="1"><stop offset="0" stop-color="#777"/><stop offset="1" stop-color="#9a9a9a"/></linearGradient>
        <linearGradient id="greenBand" x1="0" y1="0" x2="0" y2="1"><stop offset="0" stop-color="#a9d24a"/><stop offset="1" stop-color="#8cc234"/></linearGradient>
      </defs>
      <path d="M0 0H553V44C440 48 300 88 0 108Z" fill="url(#greyTop)"/>
      <path d="M0 112C300 92 440 52 553 48" fill="none" stroke="#9ccb3b" stroke-width="5"/>
      <path d="M0 570C90 640 250 700 553 640V738H0Z" fill="url(#greenBand)"/>
      <path d="M0 566C90 636 250 696 553 636" fill="none" stroke="#3a3a3a" stroke-width="3"/>
      <rect x="0" y="738" width="553" height="36" fill="#3a3a3a"/>
      <rect x="0" y="774" width="553" height="4" fill="#9ccb3b"/>
    </svg>

    <div class="brand">
      <span class="brand__dot"></span>
      <span class="brand__name">Pedal Haven</span>
    </div>

    <h1 class="headline">
      <div class="headline__line">Why make biking customers</div>
      <div class="headline__accent">and their $$$</div>
      <div class="headline__line">Welcome at your business?</div>
    </h1>

    <div class="compare compare--car">
      <div class="art" role="img" aria-label="Green outline drawing of a parked car"></div>
      <div class="tag"><b>$27.00</b><span>PER HOUR</span></div>
    </div>
    <div class="price price--car">
      <div class="price__till"></div>
      <div class="price__area">13M2</div>
      <div class="price__amount">$27.00</div>
      <div class="price__unit">PER HOUR</div>
    </div>

    <div class="compare compare--bike" style="width:370px">
      <div class="tag-row">
        <div class="tag"><b>$16.20</b><span>PER HOUR</span></div>
        <div class="tag"><b>$16.20</b><span>PER HOUR</span></div>
        <div class="tag"><b>$16.20</b><span>PER HOUR</span></div>
        <div class="tag"><b>$16.20</b><span>PER HOUR</span></div>
        <div class="tag"><b>$16.20</b><span>PER HOUR</span></div>
        <div class="tag"><b>$16.20</b><span>PER HOUR</span></div>
      </div>
      <div class="art" role="img" aria-label="Row of six parked bicycle icons"></div>
    </div>
    <div class="price price--bike">
      <div class="price__till"></div>
      <div class="price__area">13M2</div>
      <div class="price__amount">$97.20</div>
      <div class="price__unit">PER HOUR</div>
    </div>

    <div class="source">Retail Spend per hour, Harbour Street, Eastvale, Melbourne Australia; Dana Rowe</div>
    <div class="footer-url">www.pedalhaven.org</div>
  </section>

  <!-- back side -->
  <section class="card card--back">
    <div class="photo-wash" role="img" aria-label="Faint background photo of bicycles parked outside a shop"></div>
    <svg class="card__shapes" viewBox="0 0 553 778" aria-hidden="true">
      <defs>
        <linearGradient id="greyTop2" x1="0" y1="0" x2="0" y2="1"><stop offset="0" stop-color="#777"/><stop offset="1" stop-color="#9a9a9a"/></linearGradient>
        <linearGradient id="greenBand2" x1="0" y1="0" x2="0" y2="1"><stop offset="0" stop-color="#a9d24a"/><stop offset="1" stop-color="#8cc234"/></linearGradient>
      </defs>
      <path d="M0 0H553V100C420 96 250 20 0 52Z" fill="url(#greyTop2)"/>
      <path d="M0 56C250 24 420 100 553 104" fill="none" stroke="#9ccb3b" stroke-width="5"/>
      <path d="M0 675C150 655 330 700 553 668V770H0Z" fill="url(#greenBand2)"/>
      <path d="M0 672C150 652 330 697 553 665" fill="none" stroke="#3a3a3a" stroke-width="4"/>
      <rect x="0" y="770" width="553" height="8" fill="#3a3a3a"/>
    </svg>

    <h2 class="back-title">Why welcome bikes?</h2>
    <ul class="reasons">
      <li>Biking customers spend $$$ where parking’s easy.</li>
      <li>They spend $$$ locally as they must carry what they buy.</li>
      <li>Biking customers move slower, so see what your business offers.</li>
      <li>They tell friends where’s good to park and shop, where they feel welcome.</li>
      <li>You’re helping people be environmentally, budget and heart friendly – and they’ll you for it.</li>
    </ul>

    <div class="study">
      <div class="study__lead">A Melbourne study showed swapping a car park</div>
      <div class="study__rest">for six bike parks could increase the space’s retail spend</div>
      <div class="study__figure">from $27 to $97.20 an hour</div>
    </div>

    <div class="prompt"><em>Just think –</em> every bike parked by someone else’s<br><em>business could have been your customer.</em></div>

    <div class="cta">
      <div class="cta__line">See
        <svg class="cta__globe" viewBox="0 0 24 24" aria-hidden="true"><g fill="none" stroke="#fff" stroke-width="1.6"><circle cx="12" cy="12" r="10.5"/><ellipse cx="12" cy="12" rx="4.5" ry="10.5"/><path d="M1.5 12H22.5M3.5 6.5H20.5M3.5 17.5H20.5"/></g></svg>
        <span class="cta__url">pedalhaven.org.nz</span>
      </div>
      <div class="cta__sub">to see how you can become a Pedal Haven business.</div>
    </div>
  </section>

</div>
</body>
</html>
```